Design some Business Cards for Varnok Advisory

A new business card design - scope

2 sides
Side 1 - varnok logo & add what you think might be good
Side 2 - name address etc & varnok logo. Use logos for twitter if you want

Name - Gideon Marsh
Position - Managing Director
Address - Level 5, 27 Harrow Lane, Melbourne, VIC 3000
Tel - +61 3 9555 0187
Mob - +61 491 570 236
Email - gmarsh@varnok.com.au
Web - www.varnok.com.au
Twitter - twitter.com/varnokadvise
LinkedIn - au.linkedin.com/in/gideon

Font for name etc - Rockwell

Colours

Blue -Cyan 96%, Magenta 66%, Yellow 8%, Black 30%

Grey - Cyan 55%, Magenta 46%, Yellow 42%, Black 2%

Current card is Varnok Biz card Front & Back v2.0

Logos are attached - up to you to use blue or white varnok logo.

```html
<!DOCTYPE html>
<html lang="en">
<head>
<meta charset="utf-8">
<title>Varnok Advisory Business Card</title>
<link href="https://fonts.googleapis.com/css2?family=Arimo:wght@400;700&family=Montserrat:wght@300&display=swap" rel="stylesheet">
<style>
  :root {
    --brand-blue: #1d3e72;
    --text-grey: #4d4d4d;
    --card-white: #ffffff;
    --backdrop: #e6e6e6;
  }
  * { margin: 0; padding: 0; box-sizing: border-box; }
  html, body {
    width: 1200px;
    height: 799px;
    overflow: hidden;
    background: var(--backdrop);
    font-family: "Arimo", Arial, sans-serif;
  }
  .card {
    position: absolute;
    top: 120px;
    width: 300px;
    height: 540px;
    background: var(--card-white);
    box-shadow: 0 2px 8px rgba(0,0,0,0.12);
    overflow: hidden;
  }
  .card--contact { left: 270px; }
  .card--brand { left: 630px; }

  .person { position: absolute; left: 40px; top: 70px; color: var(--brand-blue); }
  .person__name { font-size: 19px; font-weight: 400; line-height: 1.2; }
  .person__role { font-size: 14px; line-height: 1.3; }

  .corner-mark {
    position: absolute; right: 24px; top: 30px;
    display: flex; align-items: center; gap: 8px;
    color: var(--brand-blue);
    font-size: 14px; font-weight: 400; letter-spacing: 0.04em;
  }
  .corner-mark__square { width: 10px; height: 10px; background: var(--brand-blue); }

  .side-tab {
    position: absolute; left: 0; top: 330px;
    width: 22px; height: 180px;
    background: var(--brand-blue);
    border-radius: 0 12px 12px 0;
  }
  .contact {
    position: absolute; left: 44px; top: 335px;
    color: var(--text-grey);
    font-size: 13.5px; line-height: 1.45;
  }
  .contact__group + .contact__group { margin-top: 16px; }
  .contact__web strong { color: var(--brand-blue); font-weight: 400; }

  .brand-wordmark {
    position: absolute; left: 50%; top: 50%;
    transform: translate(-50%, -50%) rotate(90deg);
    white-space: nowrap;
    color: var(--brand-blue);
    font-family: "Montserrat", Arial, sans-serif;
    font-weight: 300;
    font-size: 40px;
    letter-spacing: 0.18em;
    text-transform: uppercase;
  }
</style>
</head>
<body>
  <section class="card card--contact" aria-label="Business card contact side">
    <div class="corner-mark">
      <span class="corner-mark__square"></span>
      <span>Varnok Advisory</span>
    </div>
    <div class="person">
      <p class="person__name">Gideon Marsh</p>
      <p class="person__role">Managing Director</p>
    </div>
    <div class="side-tab"></div>
    <div class="contact">
      <div class="contact__group">
        <p>D : +61 3 9555 0187</p>
        <p>M : +61 491 570 236</p>
        <p>gmarsh@varnok.com.au</p>
        <p class="contact__web">www.<strong>varnok</strong>.com.au</p>
      </div>
      <div class="contact__group">
        <p>Level 5, 27 Harrow Lane,</p>
        <p>Melbourne, VIC 3000</p>
        <p>Skype : Gideonmarsh</p>
        <p>Twitter : varnokadvise</p>
      </div>
    </div>
  </section>

  <section class="card card--brand" aria-label="Business card brand side">
    <p class="brand-wordmark">Varnok Advisory</p>
  </section>
</body>
</html>
```